Business Card Design

Im electrician in melbourne after a business cards. I have no logos done. I have attached a card that i like but needs to be altered to my business name, so in the picture shows a lead plug into a socket spelling plug, i want the spelling replaced with my company name. I was thinking some thing with a charcoal back ground with yellow or green font.
I have wrote what I'd like above but feel free to try your own ideas and designs.
Industry/Entity Type
Electrician
Contact Information for Business Card
Vorn Electrical Services PTY LTD (Display on the front of card, the PTY LTD can be in small font)
REC:58104 (also on the front in small font)
Call Teodor (back i dont want my last name on the card)
Phone: 0488157093 (back
Email: vornelectricalservices@kestramail.com (back)
Domestic, Commercial, Industrial, (on the back in dot points.)
Look and feel
Each slider illustrates characteristics of the customer's brand and the style your logo design should communicate.

```html
<!DOCTYPE html>
<html lang="en">
<head>
<meta charset="utf-8">
<title>Vorn Electrical Services – Business Card</title>
<link rel="stylesheet" href="https://fonts.googleapis.com/css2?family=Open+Sans:wght@300;400;600;700&display=swap">
<style>
  :root {
    --page: #e6e4e0;
    --charcoal-dark: #333333;
    --charcoal-light: #5c5c5c;
    --white: #ffffff;
    --card-white: #fbfbfb;
    --green: #4cb848;
    --green-soft: #6cc567;
    --grey-text: #5d5d5d;
    --grey-mid: #7a7a7a;
  }
  * { box-sizing: border-box; margin: 0; padding: 0; }
  html, body {
    width: 1200px;
    height: 1184px;
    overflow: hidden;
    background: var(--page);
    font-family: "Open Sans", Arial, sans-serif;
  }
  .sheet {
    position: relative;
    width: 1200px;
    height: 1184px;
  }
  .card {
    position: absolute;
    left: 150px;
    width: 900px;
    height: 500px;
    border-radius: 4px;
    box-shadow: 0 6px 24px rgba(0,0,0,0.18);
    overflow: hidden;
  }

  /* Front: charcoal */
  .card--front {
    top: 72px;
    background: linear-gradient(115deg, var(--charcoal-dark) 0%, var(--charcoal-light) 55%, var(--charcoal-dark) 100%);
    color: var(--white);
  }
  .licence {
    position: absolute;
    top: 34px;
    left: 44px;
    font-size: 17px;
    font-weight: 400;
    letter-spacing: 3px;
    color: #d8d8d8;
  }
  .front-name {
    position: absolute;
    top: 170px;
    left: 0;
    width: 100%;
    text-align: center;
  }
  .front-name__title {
    font-size: 58px;
    font-weight: 600;
    letter-spacing: 0.5px;
    color: var(--white);
  }
  .front-name__suffix {
    margin-top: 8px;
    font-size: 16px;
    font-weight: 400;
    letter-spacing: 5px;
    color: #cfcfcf;
  }
  .services {
    position: absolute;
    bottom: 44px;
    left: 0;
    width: 100%;
    display: flex;
    justify-content: center;
    gap: 44px;
    list-style: none;
    font-size: 20px;
    font-weight: 400;
    letter-spacing: 1px;
    color: #e8e8e8;
  }
  .services li::before {
    content: "";
    display: inline-block;
    width: 8px;
    height: 8px;
    margin-right: 12px;
    border-radius: 50%;
    background: var(--green);
    vertical-align: middle;
  }

  /* Back: white */
  .card--back {
    top: 612px;
    background: var(--card-white);
  }
  .back-name {
    position: absolute;
    top: 52px;
    left: 60px;
    display: flex;
    align-items: center;
    gap: 26px;
  }
  .back-name__dot {
    width: 70px;
    height: 70px;
    border-radius: 50%;
    background: var(--green);
  }
  .back-name__title {
    font-size: 130px;
    font-weight: 300;
    line-height: 1;
    color: var(--green);
  }
  .contact {
    position: absolute;
    left: 300px;
    top: 248px;
  }
  .contact__call {
    font-size: 50px;
    font-weight: 600;
    line-height: 1.1;
  }
  .contact__call-label { color: var(--green); }
  .contact__call-name {
    color: var(--grey-text);
    font-weight: 400;
    text-transform: uppercase;
  }
  .contact__role {
    margin-top: 12px;
    font-size: 28px;
    font-weight: 400;
    letter-spacing: 2px;
    color: var(--grey-text);
  }
  .contact__divider {
    color: var(--green);
    margin: 0 8px;
  }
  .contact__email {
    margin-top: 10px;
    font-size: 25px;
    font-weight: 400;
    letter-spacing: 1.5px;
    color: var(--grey-mid);
  }
</style>
</head>
<body>
  <main class="sheet">
    <section class="card card--front" aria-label="Card front">
      <p class="licence">REC:58104</p>
      <div class="front-name">
        <h1 class="front-name__title">Vorn Electrical Services</h1>
        <p class="front-name__suffix">PTY LTD</p>
      </div>
      <ul class="services">
        <li>Domestic</li>
        <li>Commercial</li>
        <li>Industrial</li>
      </ul>
    </section>

    <section class="card card--back" aria-label="Card back">
      <div class="back-name">
        <span class="back-name__dot" aria-hidden="true"></span>
        <span class="back-name__title">Vorn</span>
      </div>
      <div class="contact">
        <p class="contact__call"><span class="contact__call-label">Call</span> <span class="contact__call-name">Teodor</span></p>
        <p class="contact__role">ELECTRICIAN<span class="contact__divider">|</span>0488157093</p>
        <p class="contact__email">vornelectricalservices@kestramail.com</p>
      </div>
    </section>
  </main>
</body>
</html>
```